Book cover design for a debut author; 'Quiet Ledgers' by Brent Hollis.

My father has written a book and I would love to gift him a bespoke front cover for it for his 60th birthday this year.
The book is a work of fiction and tells the story of two strangers (an Asian Female and a Caucasian Male) who meet on a train. After the train crashes and bursts into flames, they take the luggage of different passengers and decide to make a new life together, culminating in a murder which they believe they can get away with forever. The book is a thriller and engages the reader in suspense, excitement, anticipation and anxiety.

Target Market(s)

Thriller Fiction Readers

Font styles to use
Serif

Colors

Designer to choose colors to be used in the design.

Requirements
Must have
• A vibrant front cover with consideration over the font of both the title and author.
• I would like the train where they meet to be the main focus for the front cover. The strangers meet on a train and I’d like the cover to reflect this.
• Design must include front cover, spine and back cover with a space for blurb (to follow).
Nice to have
• A photograph based cover would I think suit the book better than an illustration.

```html
<!DOCTYPE html>
<html lang="en">
<head>
<meta charset="utf-8">
<title>Quiet Ledgers – Book Cover</title>
<link rel="stylesheet" href="https://fonts.googleapis.com/css2?family=Montserrat:wght@500;600;700;800&display=swap">
<style>
  :root {
    --bg: #e9e9e9;
    --ink: #0d0d0d;
    --yellow: #f6c623;
    --gold: #d9a928;
    --white: #ffffff;
    --dark-text: #1c1a14;
  }
  * { margin: 0; padding: 0; box-sizing: border-box; }
  html, body { width: 1200px; height: 1000px; overflow: hidden; }
  body {
    background: radial-gradient(ellipse at center, #f7f7f7 0%, var(--bg) 70%, #dcdcdc 100%);
    font-family: "Montserrat", Arial, sans-serif;
    position: relative;
  }
  .book-jacket {
    position: absolute;
    left: 160px;
    top: 195px;
    width: 880px;
    height: 610px;
    display: flex;
    box-shadow: 0 20px 40px rgba(0,0,0,0.18);
  }

  /* Back cover */
  .back-cover {
    width: 410px;
    height: 100%;
    position: relative;
    background: linear-gradient(160deg, #e8b92a 0%, var(--gold) 55%, #c99a22 100%);
    padding: 60px 46px;
    color: var(--dark-text);
  }
  .back-cover .back-photo {
    position: absolute; inset: 0;
    background: linear-gradient(180deg, rgba(255,225,110,0.35) 0%, rgba(170,130,20,0.15) 60%, rgba(255,215,90,0.3) 100%);
  }
  .back-tagline {
    position: relative;
    border: 1.5px solid var(--dark-text);
    padding: 22px 18px;
    text-align: center;
    font-weight: 800;
    font-size: 17px;
    letter-spacing: 2px;
    line-height: 1.35;
    text-transform: uppercase;
  }
  .back-blurb {
    position: relative;
    margin-top: 34px;
    font-weight: 600;
    font-size: 15px;
    letter-spacing: 1px;
    line-height: 1.45;
  }
  .back-blurb p + p { margin-top: 20px; }

  /* Spine */
  .spine {
    width: 62px;
    height: 100%;
    background: var(--ink);
    color: var(--white);
    display: flex;
    align-items: center;
    justify-content: center;
  }
  .spine-text {
    writing-mode: vertical-rl;
    font-weight: 600;
    letter-spacing: 3px;
    white-space: nowrap;
    display: flex;
    align-items: center;
    gap: 18px;
  }
  .spine-title { font-size: 30px; letter-spacing: 5px; }
  .spine-divider { width: 1.5px; height: 40px; background: var(--white); writing-mode: horizontal-tb; }
  .spine-author { font-size: 17px; }

  /* Front cover */
  .front-cover {
    width: 408px;
    height: 100%;
    position: relative;
    background: var(--ink);
    overflow: hidden;
  }
  .cover-photo {
    position: absolute;
    left: 0; top: 0;
    width: 100%; height: 420px;
    background:
      linear-gradient(180deg, rgba(13,13,13,0) 60%, var(--ink) 100%),
      linear-gradient(100deg, #1a1a1a 0%, #5a5a5a 30%, #b8b8b8 55%, #6e6e6e 80%, #222 100%);
  }
  .cover-photo .train-streak {
    position: absolute;
    left: 0; top: 150px;
    width: 100%; height: 120px;
    background: linear-gradient(90deg, rgba(246,198,35,0.2) 0%, rgba(246,198,35,0.75) 45%, rgba(246,198,35,0.55) 75%, rgba(246,198,35,0.1) 100%);
  }
  .debut-label, .front-author {
    position: absolute;
    left: 0; width: 100%;
    text-align: center;
    font-weight: 700;
    letter-spacing: 4px;
    text-transform: uppercase;
  }
  .debut-label { top: 36px; color: var(--white); font-size: 20px; }
  .front-author { top: 62px; color: var(--yellow); font-size: 27px; }
  .cover-title {
    position: absolute;
    left: 58px; top: 440px;
    font-weight: 700;
    font-size: 64px;
    line-height: 1.05;
    letter-spacing: 2px;
    text-transform: uppercase;
  }
  .cover-title .title-first { color: var(--yellow); display: block; }
  .cover-title .title-second { color: var(--white); display: block; }
</style>
</head>
<body>
  <div class="book-jacket">
    <section class="back-cover">
      <div class="back-photo" role="img" aria-label="Yellow-tinted photograph of a city street with a passing train"></div>
      <h2 class="back-tagline">The debut fiction story of who they became</h2>
      <div class="back-blurb">
        <p>After the train crashes and bursts into flames, two strangers take the luggage of different passengers to make a new life together,</p>
        <p>culminating in a murder they believe they can get away with forever. A thriller of excitement and suspense, anticipation and anxiety.</p>
      </div>
    </section>

    <section class="spine">
      <div class="spine-text">
        <span class="spine-title">Quiet Ledgers</span>
        <span class="spine-divider"></span>
        <span class="spine-author">BRENT HOLLIS</span>
      </div>
    </section>

    <section class="front-cover">
      <div class="cover-photo" role="img" aria-label="Photograph of a city building with a yellow motion-blurred train and two hands in a handshake">
        <div class="train-streak"></div>
      </div>
      <p class="debut-label">Debut Author</p>
      <p class="front-author">Brent Hollis</p>
      <h1 class="cover-title">
        <span class="title-first">Quiet</span>
        <span class="title-second">Ledgers</span>
      </h1>
    </section>
  </div>
</body>
</html>
```